New Website

New website is to be the same as Valiant Oak.

Website needs to be fully functional, with only text and logo to be added by client at a later date.

Logo has been added for reference.

Coding

Coded - Design and coding required

```html
<!DOCTYPE html>
<html lang="en">
<head>
<meta charset="utf-8">
<title>Corvana Expert Candidate Application</title>
<link rel="stylesheet" href="https://fonts.googleapis.com/css2?family=Roboto:ital,wght@0,300;0,400;0,500;1,400&family=Open+Sans:ital,wght@0,400;0,600;1,600&display=swap">
<style>
:root{
  --blue:#3f5ea9;
  --navy:#2c4482;
  --sky:#63c6e6;
  --panel:#f1f2f2;
  --panel-alt:#e9eaea;
  --ink:#333;
  --muted:#555;
  --line:#9a9a9a;
  --white:#fff;
}
*{box-sizing:border-box;margin:0;padding:0}
html,body{width:903px;height:1200px;overflow:hidden;background:var(--white)}
body{position:relative;font-family:"Roboto",Arial,sans-serif;color:var(--ink)}
.abs{position:absolute}

/* header */
.brand-mark{left:140px;top:12px;width:50px;height:50px;border-radius:50%;background:var(--blue);border:4px solid var(--white);box-shadow:0 0 0 1px #dfe6f2;z-index:2}
.brand-name{left:198px;top:19px;font-size:23px;font-weight:400;color:var(--blue);letter-spacing:.5px}
.nav{top:27px;font-size:11.5px;color:#444}
.btn-top{top:20px;height:18px;width:55px;background:var(--blue);color:var(--white);font-size:8.5px;display:flex;align-items:center;justify-content:center}
.or{left:692px;top:24px;font-size:8px;color:#777}
.band{left:0;top:46px;width:903px;height:30px;background:var(--blue)}
.make-expert{left:492px;top:46px;width:138px;height:30px;background:var(--navy);color:var(--white);font-size:12px;display:flex;align-items:center;justify-content:center;gap:6px}
.find-expert{left:630px;top:46px;width:136px;height:35px;background:var(--sky);color:var(--white);font-size:12.5px;display:flex;align-items:center;justify-content:center;gap:7px}

/* form */
.sheet{left:137px;top:76px;width:629px;height:697px;background:var(--panel)}
.band-alt{left:137px;top:312px;width:629px;height:127px;background:var(--panel-alt)}
.title{font-size:14px;color:var(--blue);font-weight:400}
.sub{font-size:11px;color:var(--ink);font-weight:400}
.label{font-size:7px;color:var(--ink)}
.field{height:19px;background:var(--white);border:1px solid var(--line)}
.note{font-size:5px;line-height:6.5px;color:var(--muted)}
.note-lg{font-size:7px;line-height:9px;color:var(--ink)}
.help{width:15px;height:15px;border-radius:50%;background:#222;color:var(--white);font-size:10px;font-weight:700;display:flex;align-items:center;justify-content:center}
.select{font-size:7px;color:#555;display:flex;align-items:center;justify-content:space-between;padding:0 6px}
.submit{left:154px;top:712px;width:153px;height:18px;background:var(--blue);color:var(--white);font-size:8.5px;display:flex;align-items:center;justify-content:center;gap:7px}

/* footer */
.col{top:773px;height:371px}
.col-links{left:137px;width:209px;background:linear-gradient(180deg,var(--sky) 0%,var(--sky) 38%,#5ab3dd 100%);overflow:hidden}
.col-think{left:347px;width:209px;background:var(--blue);text-align:center;color:var(--white)}
.col-help{left:557px;width:209px;background:var(--navy);color:var(--white)}
.deco{left:0;top:150px;width:209px;height:221px;background:radial-gradient(circle at 30% 40%,rgba(255,255,255,.22),rgba(255,255,255,0) 60%)}
.foot-links{left:16px;top:22px;font-size:26px;line-height:35px;color:var(--white);font-weight:400}
.foot-h{font-size:22px;font-weight:400;line-height:26px}
.quote{font-family:"Open Sans",sans-serif;font-size:8px;line-height:12.2px;padding:0 16px}
.quote-mark{font-family:Georgia,serif;font-size:18px;font-weight:700;line-height:0;vertical-align:-5px}
.quote-date{font-family:"Open Sans",sans-serif;font-size:7.5px;font-weight:600;margin-top:3px}
.quote-by{font-family:"Open Sans",sans-serif;font-size:7.5px;font-weight:600;font-style:italic;margin-top:3px}
.body-copy{font-family:"Open Sans",sans-serif;font-size:7.6px;line-height:12.2px}
.social{width:26px;height:26px;border-radius:50%;top:1071px}
.legal{top:1164px;font-size:7px;color:#333}
</style>
</head>
<body>

<header>
  <div class="abs brand-mark" aria-hidden="true"></div>
  <div class="abs brand-name">CORVANA</div>
  <nav>
    <span class="abs nav" style="left:352px">How it Works</span>
    <span class="abs nav" style="left:432px">Products</span>
    <span class="abs nav" style="left:491px">Blog</span>
    <span class="abs nav" style="left:529px">Help</span>
  </nav>
  <div class="abs btn-top" style="left:630px">Sign In</div>
  <span class="abs or">OR</span>
  <div class="abs btn-top" style="left:711px">Register</div>
  <div class="abs band"></div>
  <div class="abs make-expert">
    <svg width="7" height="5" viewBox="0 0 7 5"><path d="M0 0h7L3.5 5z" fill="#fff"/></svg>Make Me An Expert
  </div>
  <div class="abs find-expert">
    <svg width="12" height="12" viewBox="0 0 12 12"><circle cx="5" cy="5" r="3.7" fill="none" stroke="#fff" stroke-width="1.8"/><path d="M7.7 7.7L11 11" stroke="#fff" stroke-width="2" stroke-linecap="round"/></svg>Find Your Expert
  </div>
</header>

<main>
  <div class="abs sheet"></div>
  <div class="abs band-alt"></div>

  <h1 class="abs title" style="left:154px;top:94px">Corvana Expert Candidate Application</h1>
  <h2 class="abs sub" style="left:154px;top:129px">About You</h2>

  <span class="abs label" style="left:154px;top:157px">Frist Name*</span>
  <div class="abs field" style="left:154px;top:167px;width:226px"></div>
  <div class="abs help" style="left:383px;top:169px">?</div>
  <span class="abs label" style="left:154px;top:195px">Last Name*</span>
  <div class="abs field" style="left:154px;top:205px;width:226px"></div>
  <span class="abs label" style="left:154px;top:232px">Phone Number*</span>
  <div class="abs field" style="left:154px;top:242px;width:226px"></div>
  <p class="abs note" style="left:154px;top:265px;width:230px">This phone number will not be made public. However, it will be used for an interview if your application is accepted.</p>

  <span class="abs label" style="left:426px;top:157px">Defaulr Time Zone*</span>
  <div class="abs field select" style="left:426px;top:167px;width:226px"><span>-- Selcet One --</span><svg width="7" height="6" viewBox="0 0 7 6"><path d="M0 0h7L3.5 6z" fill="#333"/></svg></div>
  <p class="abs note-lg" style="left:426px;top:193px;width:222px">Select your current local time zone. If in doubt, choose the timezone that is closest to your location which has the same rules for daylight saving time. Dates and times throughout this site will be displayed using this time zone.</p>

  <h2 class="abs title" style="left:154px;top:338px">Resume / Biography</h2>
  <span class="abs label" style="left:154px;top:368px">ProNet® network URL</span>
  <div class="abs field" style="left:154px;top:378px;width:226px"></div>
  <div class="abs help" style="left:383px;top:380px;background:#333">?</div>
  <p class="abs note" style="left:154px;top:401px;width:226px">By providing the URL to your ProNet® profile, we can use that as basic reference information. (ValiantOak.com is not affiliated with ProNet.com.) Your URL should look something like: http://www.pronet.com/in/yourname/</p>
  <span class="abs label" style="left:426px;top:368px">Experience / Area of Expertise</span>
  <div class="abs field" style="left:426px;top:378px;width:226px"></div>
  <p class="abs note" style="left:426px;top:401px;width:230px">Please describe below the area of expertise that you would own, develop content and consult for as a Valiant Oak Expert.<br>Include qualifications and attributes that distinguish you as an expert.</p>

  <h2 class="abs title" style="left:154px;top:458px">References</h2>

  <section>
    <h3 class="abs sub" style="left:154px;top:494px">Colleague</h3>
    <h3 class="abs sub" style="left:359px;top:494px">Client 1</h3>
    <h3 class="abs sub" style="left:566px;top:494px">Client 1</h3>

    <span class="abs label" style="left:154px;top:521px">Frist Name*</span>
    <span class="abs label" style="left:359px;top:521px">Frist Name*</span>
    <span class="abs label" style="left:566px;top:521px">Frist Name*</span>
    <div class="abs field" style="left:154px;top:531px;width:184px"></div>
    <div class="abs field" style="left:359px;top:531px;width:184px"></div>
    <div class="abs field" style="left:566px;top:531px;width:184px"></div>

    <span class="abs label" style="left:154px;top:559px">Last Name*</span>
    <span class="abs label" style="left:359px;top:559px">Last Name*</span>
    <span class="abs label" style="left:566px;top:559px">Last Name*</span>
    <div class="abs field" style="left:154px;top:569px;width:184px"></div>
    <div class="abs field" style="left:359px;top:569px;width:184px"></div>
    <div class="abs field" style="left:566px;top:569px;width:184px"></div>

    <span class="abs label" style="left:154px;top:596px">Email*</span>
    <span class="abs label" style="left:359px;top:596px">Email*</span>
    <span class="abs label" style="left:566px;top:596px">Email*</span>
    <div class="abs field" style="left:154px;top:606px;width:184px"></div>
    <div class="abs field" style="left:359px;top:606px;width:184px"></div>
    <div class="abs field" style="left:566px;top:606px;width:184px"></div>

    <span class="abs label" style="left:154px;top:634px">Telephone*</span>
    <span class="abs label" style="left:359px;top:634px">Telephone*</span>
    <span class="abs label" style="left:566px;top:634px">Telephone*</span>
    <div class="abs field" style="left:154px;top:644px;width:184px"></div>
    <div class="abs field" style="left:359px;top:644px;width:184px"></div>
    <div class="abs field" style="left:566px;top:644px;width:184px"></div>

    <span class="abs label" style="left:154px;top:673px">Company*</span>
    <span class="abs label" style="left:359px;top:673px">Company*</span>
    <span class="abs label" style="left:566px;top:673px">Company*</span>
    <div class="abs field" style="left:154px;top:683px;width:184px"></div>
    <div class="abs field" style="left:359px;top:683px;width:184px"></div>
    <div class="abs field" style="left:566px;top:683px;width:184px"></div>
  </section>

  <div class="abs submit">Submit to Corvana Review Board
    <svg width="4" height="7" viewBox="0 0 4 7"><path d="M.5 .5L3.5 3.5L.5 6.5" fill="none" stroke="#fff" stroke-width="1"/></svg>
  </div>
</main>

<footer>
  <div class="abs col col-links">
    <div class="abs deco" role="img" aria-label="Soft decorative backdrop in light blue tones"></div>
    <div class="abs foot-links">About Us<br>Our Team<br>Legal<br>Contact Us</div>
  </div>

  <div class="abs col col-think">
    <h2 class="foot-h" style="margin-top:30px">What We’re<br>Thinking</h2>
    <div style="margin-top:22px">
      <p class="quote"><span class="quote-mark">“</span> Lorem Ipsum is simply dummy text of the printing and typesetting industry. <span class="quote-mark">”</span></p>
      <p class="quote-date">Monday, January 12</p>
      <p class="quote-by">Mara Lindqvist</p>
    </div>
    <div style="margin-top:28px">
      <p class="quote"><span class="quote-mark">“</span> Lorem Ipsum is simply dummy text of the printing and typesetting industry. Lorem Ipsum has been the industry's standard dummy text ever since the 1500s, when an unknown printer took a galley of type and scrambled it to make a type specimen book. It has survived not only five centuries, but also the leap into electronic typesetting, remaining essentially unchanged. <span class="quote-mark">”</span></p>
      <p class="quote-date" style="margin-top:12px">Monday, January 12</p>
      <p class="quote-by">Owen Pratt</p>
    </div>
  </div>

  <div class="abs col col-help">
    <div style="padding:30px 14px 0 15px">
      <h2 class="foot-h">Need Help?</h2>
      <p class="body-copy" style="margin-top:14px;width:160px">Valiant Oak is committed to providing exceptional cloud-based consulting. If you need help with any aspect of the Valiant Oak experience, please send us a note and we will reply promptly. Or feel free to call our support line between 9am and 5pm Pacific Time.</p>
      <h2 class="foot-h" style="margin-top:20px">Contact Us</h2>
      <p class="body-copy" style="margin-top:13px">Valiant Oak, Inc.<br>support@valiantoak.com</p>
      <h2 class="foot-h" style="margin-top:20px">Follow us on</h2>
    </div>
  </div>
  <div class="abs social" style="left:570px;background:#3b5998" role="img" aria-label="Social network link one"></div>
  <div class="abs social" style="left:597px;background:#1da1f2" role="img" aria-label="Social network link two"></div>
  <div class="abs social" style="left:625px;background:#dd4b39" role="img" aria-label="Social network link three"></div>
  <div class="abs social" style="left:652px;background:#e52d27" role="img" aria-label="Social network link four"></div>
  <div class="abs social" style="left:679px;background:#0e76a8" role="img" aria-label="Social network link five"></div>

  <p class="abs legal" style="left:137px">© 2015 Corvana. Terms of Use and Privacy Policy</p>
</footer>

</body>
</html>
```